Digital Album Cover - Frosted Lanterns (Night Falls Still)

HiI need a digital album cover for a piano instrumental cover single

Artist: Corey Dalton
Title: Frosted Lanterns (Night Falls Still)

The song was originally by Derek Holloway

Please use my logo

You can listen to the track herehttps://soundcloud.com/coreydaltonkeys/frosted-lanterns-night-falls-still-piano-instrumental-cover

Requirements
Must have
• My logo design Corey Dalton

```html
<!DOCTYPE html>
<html lang="en">
<head>
<meta charset="utf-8">
<title>Frosted Lanterns (Night Falls Still) – Corey Dalton</title>
<link rel="stylesheet" href="https://fonts.googleapis.com/css2?family=PT+Serif:wght@700&family=Roboto:wght@500&display=swap">
<style>
  :root {
    --teal-deep: #1d4656;
    --navy-violet: #2b2552;
    --violet-mid: #6f5a9e;
    --lavender: #c7a9e4;
    --lavender-light: #dcc4f0;
    --ink: #25163a;
    --mark-fill: #25163a;
    --canvas-bg: #ffffff;
  }
  html, body {
    margin: 0;
    padding: 0;
    width: 1200px;
    height: 1200px;
    overflow: hidden;
    background: var(--canvas-bg);
  }
  .album-cover {
    position: relative;
    width: 1200px;
    height: 1200px;
    overflow: hidden;
  }
  .cover-photo {
    position: absolute;
    inset: 0;
    background:
      radial-gradient(ellipse 60% 55% at 88% 40%, var(--lavender-light) 0%, rgba(220,196,240,0) 70%),
      radial-gradient(ellipse 55% 70% at 8% 35%, rgba(29,70,86,0.95) 0%, rgba(29,70,86,0) 75%),
      linear-gradient(115deg, var(--teal-deep) 0%, var(--navy-violet) 38%, var(--violet-mid) 58%, var(--lavender) 78%, var(--lavender-light) 100%);
  }
  .artist-mark {
    position: absolute;
    left: 680px;
    top: 47px;
    display: flex;
    align-items: center;
    gap: 20px;
  }
  .artist-mark__circle {
    width: 126px;
    height: 126px;
    border-radius: 50%;
    background: var(--mark-fill);
    flex: none;
  }
  .artist-mark__name {
    font-family: "Roboto", sans-serif;
    font-weight: 500;
    font-size: 46px;
    letter-spacing: 0.5px;
    color: var(--ink);
    white-space: nowrap;
  }
  .track-title {
    position: absolute;
    left: 500px;
    width: 700px;
    top: 410px;
    margin: 0;
    font-family: "PT Serif", serif;
    font-weight: 700;
    font-size: 98px;
    line-height: 118px;
    text-align: center;
    color: var(--ink);
  }
  .track-title span { display: block; }
</style>
</head>
<body>
  <main class="album-cover">
    <div class="cover-photo" role="img" aria-label="Close-up photograph of piano keys in lavender light with soft golden bokeh lights on a dark teal left side"></div>

    <div class="artist-mark">
      <div class="artist-mark__circle" aria-hidden="true"></div>
      <div class="artist-mark__name">COREY DALTON</div>
    </div>

    <h1 class="track-title">
      <span>Frosted</span>
      <span>Lanterns</span>
      <span>(Night Falls</span>
      <span>Still)</span>
    </h1>
  </main>
</body>
</html>
```